Business Card Design Project

We are a very talented award winning hair salon, the card should be professional, classy with edge. Attached is the logo which I would like to see on one side, with text and something catchy on back.

Target Market(s)

Young professional, 20-50

Industry/Entity Type

Hair

Colors

Designer to choose colors to be used in the design.

Requirements
Must have
• Must be clean, exude professionalism, classy with some edge

```html
<!DOCTYPE html>
<html lang="en">
<head>
<meta charset="utf-8">
<title>Vela Salon — Business Card Set</title>
<link href="https://fonts.googleapis.com/css2?family=Cinzel:wght@400;500&family=Open+Sans:wght@400&display=swap" rel="stylesheet">
<style>
  :root {
    --stage: #6e4529;
    --card-black: #000000;
    --gold: #d9b03a;
    --gold-light: #f3d35e;
    --gold-deep: #b8891f;
    --name-gold: #e0a437;
    --ink: #2a2418;
    --white: #ffffff;
  }
  * { margin: 0; padding: 0; box-sizing: border-box; }
  html, body { width: 1200px; height: 806px; overflow: hidden; }
  body { background: var(--stage); font-family: "Cinzel", serif; position: relative; }

  .card {
    position: absolute;
    width: 518px;
    height: 295px;
    border-radius: 28px;
    background: var(--card-black);
    overflow: hidden;
  }
  .card--front { left: 45px; top: 37px; }
  .card--back-gold {
    left: 619px; top: 35px;
    background: linear-gradient(180deg, var(--gold-deep) 0%, var(--gold) 30%, #a77d22 45%, var(--gold) 65%, var(--gold-light) 100%);
  }
  .card--back-band { left: 49px; top: 419px; }
  .card--back-plain { left: 619px; top: 419px; }

  .card-label {
    position: absolute;
    width: 300px;
    text-align: center;
    font-family: "Open Sans", sans-serif;
    font-size: 28px;
    line-height: 36px;
    color: var(--white);
  }
  .card-label--front { left: 136px; top: 340px; }
  .card-label--back-1 { left: 705px; top: 339px; }
  .card-label--back-2 { left: 132px; top: 726px; }
  .card-label--back-3 { left: 718px; top: 735px; }

  .brand-name {
    position: absolute;
    left: 0; right: 0;
    text-align: center;
    font-family: "Cinzel", serif;
    font-weight: 400;
    font-size: 52px;
    line-height: 60px;
    letter-spacing: 6px;
    color: var(--gold);
    white-space: nowrap;
  }
  .card--front .brand-name { top: 66px; }
  .card--back-gold .brand-name { top: 122px; color: var(--ink); }
  .card--back-band .brand-name,
  .card--back-plain .brand-name { top: 122px; }

  .contact-person {
    position: absolute;
    right: 278px;
    top: 196px;
    text-align: right;
  }
  .person-name { font-size: 16px; line-height: 20px; color: var(--name-gold); letter-spacing: 0.5px; }
  .person-address { margin-top: 9px; font-size: 14px; line-height: 19px; color: var(--white); letter-spacing: 0.5px; }

  .contact-divider {
    position: absolute;
    left: 262px; top: 194px;
    width: 1px; height: 72px;
    background: var(--white);
    opacity: 0.8;
  }

  .contact-lines { position: absolute; left: 268px; top: 193px; list-style: none; }
  .contact-lines li {
    display: flex; align-items: center; gap: 4px;
    height: 26px;
    font-size: 14px;
    color: var(--white);
    white-space: nowrap;
  }
  .contact-lines svg { width: 12px; height: 12px; fill: var(--gold); flex: none; }
</style>
</head>
<body>

  <section class="card card--front" aria-label="Card front">
    <div class="brand-name">VELA SALON</div>
    <div class="contact-person">
      <p class="person-name">Your Name, Title</p>
      <p class="person-address">Street Name City Name,<br>State ZipCode</p>
    </div>
    <div class="contact-divider"></div>
    <ul class="contact-lines">
      <li>
        <svg viewBox="0 0 12 12" aria-hidden="true"><path d="M6 0a6 6 0 1 0 0 12A6 6 0 0 0 6 0zm0 1.2a4.8 4.8 0 1 1 0 9.6 4.8 4.8 0 0 1 0-9.6zM4 3l1.3-.3.8 1.7-.8.7c.4.8 1 1.4 1.8 1.8l.7-.8 1.7.8L9.2 8.2C6.4 8.4 3.6 5.6 3.8 2.8z"/></svg>
        555-014-2207
      </li>
      <li>
        <svg viewBox="0 0 12 12" aria-hidden="true"><path d="M3 1h6v1H3zM2 4h8l1 6H1z"/></svg>
        555-019-3481
      </li>
      <li>
        <svg viewBox="0 0 12 12" aria-hidden="true"><path d="M1 3h10v7H1zm1 1v.4L6 7l4-2.6V4z"/></svg>
        hello@velasalon.com
      </li>
    </ul>
  </section>
  <p class="card-label card-label--front">Front -1</p>

  <section class="card card--back-gold" aria-label="Card back, gold">
    <div class="brand-name">VELA SALON</div>
  </section>
  <p class="card-label card-label--back-1">Back -1</p>

  <section class="card card--back-band" aria-label="Card back, black">
    <div class="brand-name">VELA SALON</div>
  </section>
  <p class="card-label card-label--back-2">Back -2</p>

  <section class="card card--back-plain" aria-label="Card back, black">
    <div class="brand-name">VELA SALON</div>
  </section>
  <p class="card-label card-label--back-3">Back -3</p>

</body>
</html>
```